Business card - fitness trainer

Hello all, we have the need for a business card and would like to work with you to utilize your skills.

We would like the background to be black and use elements of the logo and lettering in blue, yellow and white, if that is possible.

Please see the attached logo which we would like to incorporate.

http://www.plinvarto.example/download-source-file.aspx?designid=5830416&type=source

I am having a hard time attaching the logo files so please let me know if you cannot see it

Thank you

Fitness

```html
<!DOCTYPE html>
<html lang="en">
<head>
<meta charset="utf-8">
<title>Fitness Trainer Business Card</title>
<link rel="stylesheet" href="https://fonts.googleapis.com/css2?family=Jost:wght@400;500;600&display=swap">
<style>
  :root {
    --stage: #1b1b1c;
    --card-dark: #1f1f20;
    --card-light: #f7f7f7;
    --brand-blue: #2f86c6;
    --brand-yellow: #f2b027;
    --ink-white: #f2f2f2;
    --ink-soft: #d6d6d6;
  }
  * { box-sizing: border-box; margin: 0; padding: 0; }
  html, body {
    width: 1200px; height: 871px; overflow: hidden;
    background: var(--stage);
    font-family: "Jost", "Futura", sans-serif;
  }
  .stage { position: relative; width: 1200px; height: 871px; }
  .card {
    position: absolute; width: 560px; height: 320px;
    border-radius: 4px; overflow: hidden;
    box-shadow: 0 18px 40px rgba(0,0,0,.55);
  }
  .card-front { left: 70px; top: 110px; background: var(--card-light); }
  .card-back  { left: 570px; top: 440px; background: var(--card-dark); }

  .brand {
    position: absolute; left: 0; right: 0; top: 50%;
    transform: translateY(-50%);
    display: flex; align-items: center; justify-content: center; gap: 14px;
  }
  .brand-dot { width: 26px; height: 26px; border-radius: 50%; background: var(--brand-yellow); }
  .brand-name { font-size: 58px; font-weight: 500; color: var(--brand-blue); letter-spacing: 1px; }

  .trainer-name {
    position: absolute; left: 200px; top: 62px; text-align: center;
    width: 320px;
  }
  .trainer-name .name {
    font-size: 28px; font-weight: 600; letter-spacing: 4px;
    color: var(--brand-yellow); text-transform: uppercase; white-space: nowrap;
  }
  .trainer-name .role {
    font-size: 19px; font-weight: 400; letter-spacing: 2px;
    color: var(--ink-white); text-transform: uppercase; margin-top: 2px;
  }
  .contact {
    position: absolute; left: 36px; top: 150px;
    font-size: 17px; line-height: 25px; letter-spacing: 1px; color: var(--ink-soft);
    list-style: none;
  }
  .accent-art {
    position: absolute; right: 0; bottom: 0;
    width: 170px; height: 150px;
    background: linear-gradient(135deg, rgba(242,242,242,.35) 0%, rgba(242,176,39,.55) 55%, rgba(31,31,32,0) 100%);
  }
</style>
</head>
<body>
<main class="stage">
  <section class="card card-front" aria-label="Card front">
    <div class="brand">
      <span class="brand-dot"></span>
      <span class="brand-name">velora</span>
    </div>
  </section>

  <section class="card card-back" aria-label="Card back">
    <div class="trainer-name">
      <p class="name">Nadia Ferrante</p>
      <p class="role">Fitness Trainer</p>
    </div>
    <ul class="contact">
      <li>Sample address 766</li>
      <li>Sample Town 01234</li>
      <li>(0) 41 555 27 80</li>
      <li>nadiaferrante@mailvora.example</li>
    </ul>
    <div class="accent-art" role="img" aria-label="Yellow and white sweeping brand artwork"></div>
  </section>
</main>
</body>
</html>
```